Veltrane Partners Website - developing a website for a new IIoT (Industrial Internet of Things) startup

Hi All-

Thought I'd re-write this bit...

Firstly, to everyone who has submitted designs, thank you.

Basically, we are looking for a simple/ elegant / modern website with clean lines and design. Because this is a startup, we don't have a great deal of content. Therefore, I'm relying on the site to give us an established / international feel (no images of London, London attractions, or the London skyline please!) We will have offices in London / LA and Tokyo by the end of this year.

Selecting great images is really important. As I say, abstract is fine (less literal.) Black and white is fine as well. We need to convey our expertise to new, international clients, so this is v.important.

http://www.pellucora41.it/ (favourite)
http://www.craftonvelmo.com/cases/

In terms of colour, I think white /grey/ black and maybe experiment with red for the word Veltrane and (possibly) Group. Please note** I need the following words / strap line written underneath the main logo: IIoT Strategy. Sensor Innovation. Machine Learning.

Whomever we chose to work with, this will be an ongoing partnership: we will continually need to add new content and update the site.

Thank you!

Tam.
Updates

**Please view updated brief description.

Target Market(s)

Mid-sized (£25M- £500M GBP) companies in the UK/ US and Asia. Facilities/ Construction/ Automotive/ Manufacturing / Engineering

Industry/Entity Type

Information Technology

Logo Text

Veltrane Partners -- IIoT Strategy. Sensor Innovation. Machine Learning (written underneath)

Coding

Coded - Design and coding required

Number of Pages Required

5+ page

Font styles to use
Sans Serif

Requirements
Must have
• An international, established, aspirational feel. Beautiful imagery. elegant infographics (nothing complex). CTA on homepage.
Should not have
• Anything cartoony / informal or naff corporate imagery.

```html
<!DOCTYPE html>
<html lang="en">
<head>
<meta charset="utf-8">
<title>Veltrane Partners — IIoT Strategy. Sensor Innovation. Machine Learning.</title>
<link rel="stylesheet" href="https://fonts.googleapis.com/css2?family=Open+Sans:wght@400;600;700&family=Montserrat:wght@500;600;700&family=Saira+Semi+Condensed:wght@400;500&display=swap">
<style>
:root{
  --ink:#333a44;
  --text:#4a4f58;
  --slate:#4e5c7c;
  --slate-dark:#3c4866;
  --navy:#2c3552;
  --blue:#4b5f8f;
  --blue-deep:#3a4c78;
  --panel:#f1f1f2;
  --line:#b9bcc6;
  --white:#ffffff;
  --charcoal:#2b2b2e;
  --green:#a9dca0;
  --footer:#ececed;
  --bar:#c7c8cc;
}
*{box-sizing:border-box;margin:0;padding:0}
html,body{width:1200px;height:3814px;overflow:hidden}
body{position:relative;background:var(--white);font-family:"Open Sans",Arial,sans-serif;color:var(--text)}
.abs{position:absolute}
svg{display:block}

/* header */
.brand{left:33px;top:28px}
.brand-name{display:flex;align-items:center;gap:8px;font-family:"Montserrat",Arial,sans-serif;font-weight:600;font-size:24px;color:var(--slate-dark);letter-spacing:.3px;line-height:1;white-space:nowrap}
.brand-dot{width:12px;height:12px;border-radius:50%;background:var(--slate)}
.brand-tag{font-size:12px;color:var(--text);margin-top:7px;white-space:nowrap}
.contact-strip{top:43px;display:flex;align-items:center;gap:7px;font-size:13px;font-weight:600;color:var(--ink);white-space:nowrap}
.social{top:42px;left:1090px;display:flex;gap:6px}
.social span{width:24px;height:24px;border-radius:50%;border:2px solid var(--slate)}

.nav{left:0;top:107px;width:1200px;height:45px;background:var(--slate)}
.nav a{position:absolute;top:0;height:45px;line-height:45px;font-family:"Montserrat",Arial,sans-serif;font-size:14px;font-weight:600;color:var(--white);text-decoration:none;letter-spacing:.3px}
.nav a.active{background:var(--charcoal);padding:0 26px}

/* hero */
.hero{left:0;top:152px;width:1200px;height:450px;background:linear-gradient(180deg,#c9ced8 0%,#b7bfcd 35%,#a8b0c0 60%,#d8dbe2 100%)}
.hero-title{left:0;top:370px;width:1200px;text-align:center;font-family:"Saira Semi Condensed",Arial,sans-serif;font-weight:500;font-size:40px;color:var(--white);white-space:nowrap;text-shadow:0 2px 6px rgba(40,50,80,.35)}
.hero-cta{left:465px;top:440px;width:270px;height:48px;border:2px solid rgba(255,255,255,.85);border-radius:12px;background:rgba(100,104,150,.75);font-family:"Saira Semi Condensed",Arial,sans-serif;font-size:22px;font-weight:500;color:var(--white);text-align:center;line-height:44px;letter-spacing:.5px}

/* section titles */
.section-title{display:flex;align-items:center;justify-content:center;gap:14px;font-family:"Montserrat",Arial,sans-serif;font-weight:600;font-size:22px;letter-spacing:1px;color:var(--slate-dark)}
.section-title .rule{width:90px;height:1px;background:var(--line)}
.section-title .mark{width:12px;height:12px;border-radius:50%;background:var(--slate)}
.section-title.light{color:var(--white)}
.section-title.light .rule{background:rgba(255,255,255,.6)}
.section-title.light .mark{background:var(--white)}
.copy{font-size:13px;line-height:1.6;color:var(--text)}

/* about */
.about-title{left:0;top:676px;width:1200px}
.about-copy{left:110px;top:742px;width:980px;text-align:center}
.about-copy p+p{margin-top:18px}

/* strategy */
.strategy-panel{left:356px;top:877px;width:844px;height:699px;background:var(--panel)}
.strategy-photo{left:13px;top:1017px;width:363px;height:432px;background:linear-gradient(135deg,#8a6a4c 0%,#b08d68 40%,#d8d4ce 70%,#6b5846 100%)}
.strategy-title{left:560px;top:995px;width:500px}
.strategy-copy{left:496px;top:1070px;width:660px}
.strategy-copy p+p{margin-top:18px}
.pill{left:636px;top:1233px;width:350px;height:42px;border-radius:6px;background:#8791b2;color:var(--white);font-size:14px;font-weight:600;text-align:center;line-height:42px}
.idea{width:170px;text-align:center;font-size:12px;line-height:1.45;color:var(--ink)}
.idea .disc{width:92px;height:92px;margin:0 auto 12px;border-radius:50%;background:#5d6171;border:5px solid #d4d5da;display:flex;align-items:center;justify-content:center}

/* sensors */
.sensors{left:0;top:1589px;width:1200px;height:597px;background:linear-gradient(180deg,#4a5e8e 0%,#5a6f9e 50%,#465a88 100%)}
.sensors-title{left:0;top:1638px;width:1200px}
.sensors-copy{left:160px;top:1706px;width:880px;text-align:center;color:var(--white)}
.sensors-copy p+p{margin-top:16px}
.node-label{font-size:12px;font-weight:600;color:var(--white);text-align:center;width:160px;line-height:1.3}
.sensor-hub{left:618px;top:1962px;width:106px;height:40px;border-radius:6px;background:var(--charcoal);color:var(--white);font-size:15px;text-align:center;line-height:40px}

/* data & ai */
.data-panel{left:0;top:2237px;width:844px;height:585px;background:var(--panel)}
.data-title{left:150px;top:2304px;width:490px}
.data-copy{left:61px;top:2378px;width:660px}
.data-photo{left:752px;top:2318px;width:433px;height:435px;background:linear-gradient(135deg,#e6e7ea 0%,#c8b8a6 35%,#7a6f68 60%,#dcdde0 100%)}
.stage{width:90px;height:94px;background:var(--white);border:2px solid #c2c6d4;border-radius:4px;text-align:center;font-family:"Montserrat",Arial,sans-serif;font-size:9.5px;font-weight:600;color:var(--slate-dark);line-height:1.25;padding-top:8px}
.stage svg{margin:0 auto 6px}

/* blog */
.blog-title{left:0;top:2888px;width:1200px}
.card{top:2956px;width:356px;height:323px;background:var(--white);box-shadow:0 10px 10px -6px rgba(0,0,0,.25)}
.card .thumb{height:183px}
.card h3{font-size:14px;font-weight:700;color:var(--charcoal);margin:20px 0 6px}
.card p{font-size:12px;line-height:1.5;color:var(--text)}
.card .more{position:absolute;right:2px;bottom:7px;width:110px;height:36px;background:#595b62;color:var(--white);font-size:12px;font-weight:600;line-height:36px;text-align:center}

/* newsletter */
.newsletter{left:0;top:3343px;width:1200px;height:145px;background:linear-gradient(90deg,#3f5284 0%,#556aa0 100%)}
.news-head{left:203px;top:3372px;font-family:"Montserrat",Arial,sans-serif;font-weight:700;font-size:24px;color:var(--white);letter-spacing:.5px;white-space:nowrap}
.news-sub{left:203px;top:3412px;width:400px;font-size:14px;font-weight:600;line-height:1.35;color:var(--white)}
.news-input{left:612px;top:3398px;width:354px;height:40px;background:var(--white);padding-left:12px;font-size:14px;font-weight:600;line-height:40px;color:var(--ink)}
.news-btn{left:976px;top:3398px;width:132px;height:40px;background:var(--charcoal);color:var(--white);font-family:"Montserrat",Arial,sans-serif;font-size:15px;font-weight:700;text-align:center;line-height:40px}

/* footer */
.footer{left:0;top:3488px;width:1200px;height:274px;background:var(--footer)}
.foot-head{font-family:"Montserrat",Arial,sans-serif;font-weight:700;font-size:15px;color:var(--charcoal)}
.foot-links{font-size:12px;font-weight:600;color:var(--charcoal);line-height:17px}
.foot-row{display:flex;align-items:flex-start;gap:12px;font-size:12px;font-weight:600;color:var(--charcoal);line-height:1.45}
.foot-icon{width:22px;height:22px;flex:none}
.field{left:572px;width:221px;background:#c4c5c9;font-size:9px;font-weight:700;color:var(--charcoal);padding:5px 8px}
.submit{left:572px;top:3709px;width:92px;height:22px;background:var(--charcoal);color:var(--white);font-size:10px;font-weight:700;text-align:center;line-height:22px}
.foot-brand{left:859px;top:3604px}
.copybar{left:0;top:3762px;width:1200px;height:52px;background:var(--bar)}
.copybar p{position:absolute;left:20px;top:19px;font-size:9px;font-weight:600;color:var(--white);letter-spacing:.4px}
.copybar .social{top:14px;left:1110px}
.copybar .social span{width:22px;height:22px;border-color:var(--white)}
</style>
</head>
<body>

<!-- header -->
<div class="abs brand">
  <div class="brand-name">VELTRANE PARTNERS<span class="brand-dot"></span></div>
  <div class="brand-tag">IIoT Strategy. Sensor Innovation. Machine Learning.</div>
</div>
<div class="abs contact-strip" style="left:690px">
  <svg width="22" height="22" viewBox="0 0 24 24"><circle cx="12" cy="12" r="11" fill="none" stroke="#333a44" stroke-width="2"/><path d="M8 6l3 3-2 2c1 2 2 3 4 4l2-2 3 3-2 2c-5 0-10-5-10-10z" fill="#333a44"/></svg>
  1-800-555-0148
</div>
<div class="abs contact-strip" style="left:850px">
  <svg width="22" height="22" viewBox="0 0 24 24"><circle cx="12" cy="12" r="11" fill="none" stroke="#333a44" stroke-width="2"/><rect x="6" y="8" width="12" height="8" fill="none" stroke="#333a44" stroke-width="1.6"/><path d="M6 8l6 5 6-5" fill="none" stroke="#333a44" stroke-width="1.6"/></svg>
  info@veltranepartners.com
</div>
<div class="abs social"><span></span><span></span><span></span></div>

<nav class="abs nav">
  <a class="active" style="left:145px">HOME</a>
  <a style="left:280px">ABOUT</a>
  <a style="left:381px">STRATEGY</a>
  <a style="left:508px">SENSORS</a>
  <a style="left:630px">DATA &amp; AI</a>
  <a style="left:752px">EVENTS</a>
  <a style="left:864px">BLOG</a>
  <a style="left:953px">CONTACT</a>
</nav>

<!-- hero -->
<div class="abs hero" role="img" aria-label="Businessman standing before a hazy city skyline seen through tall windows"></div>
<h1 class="abs hero-title">IIoT Strategy. Sensor Innovation. Machine Learning.</h1>
<div class="abs hero-cta">GET STARTED NOW</div>

<!-- about -->
<h2 class="abs section-title about-title"><span class="rule"></span><span class="mark"></span>ABOUT VELTRANE PARTNERS<span class="rule"></span></h2>
<div class="abs copy about-copy">
  <p>The core team at Veltrane Partners are Innovators, Engineers, PhDs and Data Scientists who assist mid-sized companies ($25M–$500M) to capitalise on the enormous potential of the Industrial Internet of Things ("IIoT.")</p>
  <p>Our three business units – Strategy, Sensors and AI – mean that we can provide expert advice to both new entrants and companies already familiar with IIoT. Founded by our Chief Strategy Officer and serial entrepreneur, Tam Vesko, Veltrane is based in London and have plans to open offices in Tokyo and LA in late 2017.</p>
</div>

<!-- strategy -->
<div class="abs strategy-panel"></div>
<div class="abs strategy-photo" role="img" aria-label="Overhead view of a team working around a wooden table with laptops and charts"></div>
<h2 class="abs section-title strategy-title"><span class="rule"></span><span class="mark"></span>STRATEGY<span class="rule"></span></h2>
<div class="abs copy strategy-copy">
  <p>The Strategy team work with customers to navigate the complex world of IIoT and develop world-class strategies for maximising value. We know that connecting assets is not appropriate for every business: sometimes the challenges outweigh the rewards.</p>
  <p>However, where an IIoT strategy is appropriate we have the right team to help your company clarify its visions, goals &amp; guiding principles and manage the IIoT roadmap in partnership with your senior team.</p>
</div>
<div class="abs pill">Ideas for IIoT Strategy Development</div>

<div class="abs idea" style="left:474px;top:1309px">
  <div class="disc"><svg width="44" height="44" viewBox="0 0 44 44" fill="none" stroke="#fff" stroke-width="2.5"><path d="M6 10h32M6 22h32M6 34h32"/><circle cx="14" cy="10" r="3" fill="#5d6171"/><circle cx="28" cy="22" r="3" fill="#5d6171"/><circle cx="18" cy="34" r="3" fill="#5d6171"/></svg></div>
  Opportunities for quality and maintenance improvements
</div>
<div class="abs idea" style="left:662px;top:1309px">
  <div class="disc"><svg width="46" height="46" viewBox="0 0 46 46" fill="#fff" stroke="#fff" stroke-width="2.5"><path d="M23 23L10 10M23 23L36 10M23 23L10 36M23 23L36 36"/><circle cx="23" cy="23" r="5"/><circle cx="9" cy="9" r="4"/><circle cx="37" cy="9" r="4"/><circle cx="9" cy="37" r="4"/><circle cx="37" cy="37" r="4"/></svg></div>
  Potential for offering new services to customers
</div>
<div class="abs idea" style="left:835px;top:1309px">
  <div class="disc"><svg width="44" height="44" viewBox="0 0 44 44" fill="none" stroke="#fff" stroke-width="2.5"><path d="M10 6h18l8 8v24H10z"/><circle cx="22" cy="24" r="6"/><path d="M26 28l6 6"/></svg></div>
  Investigating new data, service or product-centric business models
</div>
<div class="abs idea" style="left:1008px;top:1309px">
  <div class="disc"><svg width="44" height="44" viewBox="0 0 44 44" fill="#fff"><rect x="8" y="28" width="6" height="10"/><rect x="17" y="22" width="6" height="16"/><rect x="26" y="15" width="6" height="23"/><rect x="35" y="8" width="4" height="30"/></svg></div>
  Developing new revenue streams
</div>

<!-- sensors -->
<div class="abs sensors" role="img" aria-label="Blue-toned image of a hand touching a digital analytics interface"></div>
<h2 class="abs section-title light sensors-title"><span class="rule"></span><span class="mark"></span>SENSORS<span class="rule"></span></h2>
<div class="abs copy sensors-copy">
  <p>The Sensor team are focused on Innovation using Sensors and MEMS (Micro-Electromechanical Systems.) We view ourselves as the conduit between the vast array of complex sensors and their potential applications in the 'real world.'</p>
  <p>Our main focus is looking at sensor deployments for Buildings, Environment, Factories, Parking, Agriculture, Water, Air and Health.</p>
</div>
<svg class="abs" style="left:220px;top:1850px" width="860" height="220" viewBox="0 0 860 220">
  <rect x="34" y="36" width="788" height="148" rx="14" fill="none" stroke="#fff" stroke-width="3"/>
  <g fill="#fff" stroke="#cfd6e6" stroke-width="3">
    <circle cx="34" cy="115" r="28"/>
    <circle cx="103" cy="36" r="28"/><circle cx="283" cy="36" r="28"/><circle cx="451" cy="36" r="28"/><circle cx="621" cy="36" r="28"/><circle cx="789" cy="36" r="28"/>
    <circle cx="115" cy="184" r="28"/><circle cx="283" cy="184" r="28"/><circle cx="451" cy="184" r="28"/><circle cx="621" cy="184" r="28"/><circle cx="789" cy="184" r="28"/>
  </g>
  <g fill="none" stroke="#5a6f9e" stroke-width="2.5" stroke-linecap="round">
    <circle cx="28" cy="109" r="6"/><circle cx="42" cy="121" r="6"/>
    <path d="M98 26h10M100 26v8l-8 14h22l-8-14v-8"/>
    <path d="M275 30l8-8 8 8M291 42l-8 8-8-8M283 22v28"/>
    <path d="M437 44a14 14 0 0 1 28 0M451 44l6-10"/>
    <path d="M607 28h28M607 36h28M607 44h28"/><circle cx="615" cy="28" r="2.5"/><circle cx="627" cy="44" r="2.5"/>
    <path d="M789 20a8 8 0 0 0-8 8 8 8 0 0 0 8 24 8 8 0 0 0 8-24 8 8 0 0 0-8-8z"/>
    <path d="M115 170a10 10 0 0 1 10 10c0 8-10 18-10 18s-10-10-10-18a10 10 0 0 1 10-10z"/>
    <path d="M272 178h6l8-8v28l-8-8h-6zM292 176a10 10 0 0 1 0 16"/>
    <path d="M443 174c-4 6-6 9-6 11a6 6 0 0 0 12 0c0-2-2-5-6-11zM459 174c-4 6-6 9-6 11a6 6 0 0 0 12 0c0-2-2-5-6-11z"/>
    <path d="M609 196h24M621 170v18M615 182l6 6 6-6"/>
    <path d="M789 170c-6 8-9 12-9 16a9 9 0 0 0 18 0c0-4-3-8-9-16z"/>
  </g>
</svg>
<div class="abs node-label" style="left:243px;top:1834px">Chemical &amp; Gas</div>
<div class="abs node-label" style="left:423px;top:1834px">Motion/Velocity</div>
<div class="abs node-label" style="left:591px;top:1834px">Acceleration</div>
<div class="abs node-label" style="left:761px;top:1834px">Levels &amp; Leaks</div>
<div class="abs node-label" style="left:929px;top:1834px">Temperature</div>
<div class="abs node-label" style="left:110px;top:1957px;width:110px;text-align:right">Machine Vision</div>
<div class="abs node-label" style="left:255px;top:2072px">Proximity/Presence/<br>Position</div>
<div class="abs node-label" style="left:423px;top:2072px">Sound/Vibration</div>
<div class="abs node-label" style="left:591px;top:2072px">Water/Liquid Flow</div>
<div class="abs node-label" style="left:761px;top:2072px">Pressure/Force/Load</div>
<div class="abs node-label" style="left:929px;top:2072px">Moisture &amp; Humidity</div>
<div class="abs sensor-hub">Sensors</div>

<!-- data & ai -->
<div class="abs data-panel"></div>
<h2 class="abs section-title data-title"><span class="rule"></span><span class="mark"></span>DATA &amp; AI<span class="rule"></span></h2>
<div class="abs copy data-copy">The Data &amp; AI team focus on getting the maximum value from our customer's sensors. We are a small team of engineers and data scientists who know that the real value from IIoT comes from the quality of sensor data. We monitor and analyse this data and then deliver it to our customers via stunning dashboards.</div>
<div class="abs data-photo" role="img" aria-label="Smiling business team gathered around a laptop in a bright office"></div>

<svg class="abs" style="left:30px;top:2470px" width="700" height="310" viewBox="0 0 700 310">
  <path d="M46 283L560 120" stroke="#a9dca0" stroke-width="10" stroke-linecap="round"/>
  <path d="M548 106l28 10-22 20z" fill="#a9dca0"/>
  <text x="470" y="130" font-family="Montserrat, sans-serif" font-size="11" fill="#7fbf75" font-weight="600">VALUE</text>
  <line x1="41" y1="169" x2="660" y2="169" stroke="#8f93a0" stroke-width="2.5"/>
  <circle cx="41" cy="169" r="6" fill="#8f93a0"/><circle cx="660" cy="169" r="6" fill="#8f93a0"/>
  <g stroke="#b5b9c6" stroke-width="2"><line x1="133" y1="110" x2="133" y2="169"/><line x1="344" y1="110" x2="344" y2="169"/><line x1="578" y1="110" x2="578" y2="169"/><line x1="227" y1="169" x2="227" y2="212"/><line x1="462" y1="169" x2="462" y2="212"/></g>
  <g fill="#fff" stroke="#8f93a0" stroke-width="2.5">
    <circle cx="117" cy="169" r="14"/><circle cx="229" cy="169" r="14"/><circle cx="346" cy="169" r="14"/><circle cx="461" cy="169" r="14"/><circle cx="580" cy="169" r="14"/>
  </g>
  <g fill="none" stroke="#5d6171" stroke-width="2.5" stroke-linecap="round">
    <path d="M110 169h12M118 164l5 5-5 5"/><path d="M222 169h12M230 164l5 5-5 5"/><path d="M339 169h12M347 164l5 5-5 5"/><path d="M454 169h12M462 164l5 5-5 5"/><path d="M573 169h12M581 164l5 5-5 5"/>
  </g>
</svg>
<div class="abs stage" style="left:41px;top:2517px;width:53px;height:50px;padding-top:6px;background:#8791b2;border-color:#8791b2;color:#fff;font-size:7.5px">
  <svg width="18" height="18" viewBox="0 0 18 18"><circle cx="9" cy="9" r="6" fill="none" stroke="#fff" stroke-width="2"/><circle cx="9" cy="9" r="2" fill="#fff"/></svg>SENSORS
</div>
<div class="abs stage" style="left:118px;top:2486px">
  <svg width="34" height="30" viewBox="0 0 34 30" fill="none" stroke="#4e5c7c" stroke-width="2"><rect x="3" y="3" width="28" height="22"/><path d="M8 10h18M8 15h18M8 20h12"/></svg>RICH DATA
</div>
<div class="abs stage" style="left:329px;top:2486px">
  <svg width="34" height="30" viewBox="0 0 34 30" fill="#4e5c7c"><rect x="4" y="17" width="5" height="10"/><rect x="12" y="11" width="5" height="16"/><rect x="20" y="14" width="5" height="13"/><rect x="28" y="6" width="4" height="21"/></svg>HISTORICAL<br>ANALYTICS
</div>
<div class="abs stage" style="left:563px;top:2486px">
  <svg width="34" height="30" viewBox="0 0 34 30" fill="none" stroke="#4e5c7c" stroke-width="2"><circle cx="15" cy="16" r="11"/><circle cx="15" cy="16" r="6"/><circle cx="15" cy="16" r="1.5" fill="#4e5c7c"/><path d="M15 16L30 3"/></svg>INTELLIGENT<br>DECISION MAKING
</div>
<div class="abs stage" style="left:212px;top:2682px">
  <svg width="34" height="30" viewBox="0 0 34 30" fill="none" stroke="#4e5c7c" stroke-width="2"><rect x="3" y="4" width="28" height="18"/><path d="M12 27h10M17 22v5M6 16l6-5 5 4 8-8"/></svg>REALTIME<br>ANALYTICS
</div>
<div class="abs stage" style="left:447px;top:2682px">
  <svg width="34" height="30" viewBox="0 0 34 30" fill="#4e5c7c"><rect x="4" y="18" width="5" height="9"/><rect x="12" y="13" width="5" height="14"/><rect x="20" y="8" width="5" height="19"/><path d="M4 12L24 2" stroke="#4e5c7c" stroke-width="2"/></svg>PREDICTIVE<br>ANALYTICS
</div>

<!-- blog -->
<h2 class="abs section-title blog-title"><span class="rule"></span><span class="mark"></span>BLOG<span class="rule"></span></h2>
<article class="abs card" style="left:48px">
  <div class="thumb" role="img" aria-label="Dancer leaping in front of a wall of digital screens" style="background:linear-gradient(135deg,#dfe3ea 0%,#9ea7b8 50%,#c9cfd9 100%)"></div>
  <h3>News Title #1</h3>
  <p>Lorem ipsum dolor sit amet, consectetuer adipiscing elit, sed diam nonummy nibh euismod tincidunt ut laoreet dolore magna aliquam erat volutpat.</p>
  <div class="more">READ MORE ›</div>
</article>
<article class="abs card" style="left:422px">
  <div class="thumb" role="img" aria-label="Glowing blue circuit board with a central processor" style="background:radial-gradient(circle at 50% 55%,#4aa3e8 0%,#1c4f9a 45%,#0b1f48 100%)"></div>
  <h3>News Title #2</h3>
  <p>Lorem ipsum dolor sit amet, consectetuer adipiscing elit, sed diam nonummy nibh euismod tincidunt ut laoreet dolore magna aliquam erat volutpat.</p>
  <div class="more">READ MORE ›</div>
</article>
<article class="abs card" style="left:796px">
  <div class="thumb" role="img" aria-label="Hand drawing a rising line graph on a glass screen" style="background:linear-gradient(135deg,#ffffff 0%,#e9ebef 60%,#bfc3cc 100%)"></div>
  <h3>News Title #3</h3>
  <p>Lorem ipsum dolor sit amet, consectetuer adipiscing elit, sed diam nonummy nibh euismod tincidunt ut laoreet dolore magna aliquam erat volutpat.</p>
  <div class="more">READ MORE ›</div>
</article>

<!-- newsletter -->
<div class="abs newsletter"></div>
<svg class="abs" style="left:97px;top:3390px" width="82" height="68" viewBox="0 0 82 68" fill="none" stroke="#fff" stroke-width="4" stroke-linejoin="round"><path d="M4 26L41 4l37 22v38H4z"/><path d="M4 26l37 24 37-24M4 64l28-22M78 64L50 42"/></svg>
<div class="abs news-head">SUBSCRIBE TO NEWSLETTER</div>
<div class="abs news-sub">We will be launching some exclusive invite-only events in 2018. If you would like to know, please enter your email address here.</div>
<div class="abs news-input">Email Address</div>
<div class="abs news-btn">SIGN ME UP</div>

<!-- footer -->
<footer class="abs footer"></footer>
<div class="abs foot-head" style="left:69px;top:3530px">QUICK LINKS</div>
<div class="abs foot-links" style="left:69px;top:3578px">HOME<br>ABOUT<br>STRATEGY<br>SENSORS</div>
<div class="abs foot-links" style="left:183px;top:3578px">DATA &amp; AI<br>EVENTS<br>BLOG<br>CONTACT</div>

<div class="abs foot-head" style="left:325px;top:3530px">CONTACT</div>
<div class="abs foot-row" style="left:325px;top:3574px"><svg class="foot-icon" viewBox="0 0 22 22"><circle cx="11" cy="11" r="10" fill="none" stroke="#2b2b2e" stroke-width="2"/><path d="M11 5a4 4 0 0 1 4 4c0 3-4 8-4 8s-4-5-4-8a4 4 0 0 1 4-4z" fill="#2b2b2e"/></svg><div>VELTRANE PARTNERS<br>48 HARBOR ROW<br>LOS ANGELES, CA 90017</div></div>
<div class="abs foot-row" style="left:325px;top:3666px;align-items:center"><svg class="foot-icon" viewBox="0 0 22 22"><circle cx="11" cy="11" r="10" fill="none" stroke="#2b2b2e" stroke-width="2"/><path d="M7 5l3 3-2 2c1 2 2 3 4 4l2-2 3 3-2 2c-5 0-9-4-9-9z" fill="#2b2b2e"/></svg>1.800.555.0148</div>
<div class="abs foot-row" style="left:325px;top:3704px;align-items:center"><svg class="foot-icon" viewBox="0 0 22 22"><circle cx="11" cy="11" r="10" fill="none" stroke="#2b2b2e" stroke-width="2"/><rect x="5" y="7" width="12" height="8" fill="none" stroke="#2b2b2e" stroke-width="1.6"/><path d="M5 7l6 5 6-5" fill="none" stroke="#2b2b2e" stroke-width="1.6"/></svg>info@veltranepartners.com</div>

<div class="abs foot-head" style="left:572px;top:3530px">SEND A MESSAGE</div>
<div class="abs field" style="top:3579px;height:21px">NAME</div>
<div class="abs field" style="top:3612px;height:23px">EMAIL</div>
<div class="abs field" style="top:3645px;height:54px">MESSAGE</div>
<div class="abs submit">SUBMIT</div>

<div class="abs brand foot-brand">
  <div class="brand-name">VELTRANE PARTNERS<span class="brand-dot"></span></div>
  <div class="brand-tag">IIoT Strategy. Sensor Innovation. Machine Learning.</div>
</div>

<div class="abs copybar">
  <p>COPYRIGHT © 2017 VELTRANE PARTNERS. ALL RIGHTS RESERVED</p>
  <div class="abs social"><span></span><span></span><span></span></div>
</div>

</body>
</html>
```